VMR business card

Need a business card for a company that provides instructional design and elearning development services. The website is here: http://vantmoro.studio/

I'm attaching a current logo, as well as the old business card design. While I like to keep it clean, the old design is too simplistic for my liking. The only idea I want to reuse from the old design is placing industry jargon on the back of the card, just need a better way to present it. But if you have other ideas for the back--feel free to experiment.

Please use the colors complementary to the color we have on the website. Thank you!

```html
<!DOCTYPE html>
<html lang="en">
<head>
<meta charset="utf-8">
<title>VMR business card</title>
<link href="https://fonts.googleapis.com/css2?family=Open+Sans:wght@400;600;700&display=swap" rel="stylesheet">
<style>
  :root {
    --backdrop: #3b3431;
    --card: #0b0b0b;
    --teal: #1bbdb3;
    --teal-soft: #7fd3b8;
    --sand: #e8e08f;
    --ink: #f2f2f2;
    --silver: #d9d9d9;
  }
  * { box-sizing: border-box; margin: 0; padding: 0; }
  html, body {
    width: 1200px; height: 900px; overflow: hidden;
    background: var(--backdrop);
    font-family: "Open Sans", Arial, sans-serif;
  }
  .stage {
    position: relative; width: 1200px; height: 900px;
    display: flex; align-items: center; justify-content: center; gap: 50px;
  }
  .card {
    position: relative; width: 525px; height: 300px;
    background: var(--card);
    box-shadow: 0 14px 30px rgba(0,0,0,.45);
    color: var(--ink);
  }
  /* front */
  .brand-mark {
    position: absolute; left: 50px; top: 118px;
    display: flex; align-items: center; gap: 14px;
  }
  .brand-mark .dot {
    width: 26px; height: 26px; border-radius: 50%;
    background: linear-gradient(180deg, var(--teal), var(--sand));
  }
  .brand-mark .name {
    font-size: 52px; font-weight: 700; color: var(--teal); letter-spacing: 2px;
  }
  .divider {
    position: absolute; left: 248px; top: 82px; width: 1px; height: 140px;
    background: linear-gradient(180deg, transparent, var(--teal) 30%, var(--teal) 70%, transparent);
  }
  .contact { position: absolute; left: 272px; top: 92px; }
  .contact .person {
    font-size: 17px; font-weight: 600; color: var(--teal); margin-bottom: 22px;
  }
  .contact ul { list-style: none; }
  .contact li {
    display: flex; align-items: center; gap: 10px;
    font-size: 13.5px; line-height: 22px;
  }
  .contact svg { width: 11px; height: 11px; fill: var(--teal); flex: none; }
  /* back */
  .card.back { text-align: center; }
  .back .brand-mark {
    position: static; justify-content: center; margin-top: 52px;
  }
  .back .brand-mark .name { color: var(--silver); font-size: 46px; }
  .back .brand-mark .dot { background: var(--silver); width: 22px; height: 22px; }
  .services-title {
    margin-top: 20px; font-size: 14px; font-weight: 700; letter-spacing: .3px;
  }
  .services { list-style: none; margin-top: 6px; }
  .services li { font-size: 12.5px; line-height: 17px; color: var(--ink); }
</style>
</head>
<body>
<main class="stage">
  <section class="card front" aria-label="Card front">
    <div class="brand-mark">
      <span class="dot"></span>
      <span class="name">VMR</span>
    </div>
    <div class="divider"></div>
    <div class="contact">
      <p class="person">Marcus Delvane</p>
      <ul>
        <li>
          <svg viewBox="0 0 24 24" aria-hidden="true"><path d="M6.6 10.8a15.1 15.1 0 0 0 6.6 6.6l2.2-2.2a1 1 0 0 1 1-.25 11.4 11.4 0 0 0 3.6.6 1 1 0 0 1 1 1V20a1 1 0 0 1-1 1A17 17 0 0 1 3 4a1 1 0 0 1 1-1h3.5a1 1 0 0 1 1 1c0 1.25.2 2.45.6 3.6a1 1 0 0 1-.25 1z"/></svg>
          555-013-2740
        </li>
        <li>
          <svg viewBox="0 0 24 24" aria-hidden="true"><path d="M2 5h20v14H2z M2 5l10 8 10-8" stroke="#0b0b0b" stroke-width="1.5"/></svg>
          mdelvane@vantmoro.studio
        </li>
        <li>
          <svg viewBox="0 0 24 24" aria-hidden="true"><circle cx="12" cy="12" r="10"/><path d="M2 12h20M12 2c3 3 3 17 0 20M12 2c-3 3-3 17 0 20" stroke="#0b0b0b" stroke-width="1.5" fill="none"/></svg>
          www.vantmoro.studio
        </li>
      </ul>
    </div>
  </section>

  <section class="card back" aria-label="Card back">
    <div class="brand-mark">
      <span class="dot"></span>
      <span class="name">VMR</span>
    </div>
    <h2 class="services-title">HOW CAN WE HELP?</h2>
    <ul class="services">
      <li>Mobile Learning Scorm</li>
      <li>Instructional Design Lms</li>
      <li>Moocs Elearning Html5</li>
      <li>Adult Learning Theory</li>
      <li>Gamification Classroom</li>
      <li>Xapi Blended Learning</li>
    </ul>
  </section>
</main>
</body>
</html>
```